new KVR one page flyer

We need a 1 page A4 size flyer (need it asap please) that describes on 1 page with art work and using photos the services we provide. I have included some examples of old previous flyers from our other (seperate divisions of the business) I have named a photo called (photo for top of design) however you do your design this photo needs to be the star of the page by either having it at the top or bottom of the page please and we usually like this photo to be in greyscale colour.
we do like greyscale designs but are open to see what you come up with as a whole page of grey white and black might not suit.

Needs to list the following

Services include:
Over size loads / Hot Shot Loads
Heavy Vehicle Recovery services
Potable Water Deliveries
Road Building / Maintenance
Earthworks
Sand & Metal Supply & Cartage
Road Train Tippers
Road Train Tankers
Road Train Flat Tops
Drop Deck Trailers
Mine site accredited equipment & Operators.

We offer a large rage of services not listed so call us today for a personalised quote to suit your needs.

To go on the bottom of the page our contact details are

KVR Pty Ltd
Depot: Lot 514, Banksia Flats Track Coober Pedy
Mobile: 047 216 9381
email: darren@kestrelvaleroadworks.com.au

Target Market(s)

new clients

Colors

Designer to choose colors to be used in the design.

Requirements
Must have
• our services listed
Nice to have
• stand out designs

```html
<!DOCTYPE html>
<html lang="en">
<head>
<meta charset="utf-8">
<title>KVR Services Flyer</title>
<link rel="stylesheet" href="https://fonts.googleapis.com/css2?family=Bebas+Neue&family=Lato:wght@400;700&display=swap">
<style>
  :root {
    --ink: #1c1c1c;
    --black: #0e0e0e;
    --gold: #a97b35;
    --grey-dark: #4a4a4a;
    --grey-mid: #8a8a8a;
    --paper: #ffffff;
    --silver: #cfcfcf;
    --footer-text: #ececec;
  }
  * { margin: 0; padding: 0; box-sizing: border-box; }
  html, body { width: 1049px; height: 1200px; overflow: hidden; background: var(--paper); }
  .flyer { position: relative; width: 1049px; height: 1200px; overflow: hidden; background: var(--paper); font-family: "Lato", sans-serif; color: var(--ink); }
  .hero { position: absolute; left: 0; top: 0; width: 1049px; height: 442px; display: block; }
  .gallery { position: absolute; left: 19px; top: 467px; width: 406px; }
  .gallery-photo {
    width: 406px; height: 155px; margin-bottom: 10px;
    border: 1px solid var(--grey-mid);
    background: linear-gradient(180deg, #d8d8d8 0%, #b4b4b4 50%, #9a9a9a 62%, #c2c2c2 100%);
  }
  .services { position: absolute; left: 469px; top: 466px; width: 565px; }
  .services-title { font-family: "Bebas Neue", sans-serif; font-size: 50px; line-height: 1; color: var(--ink); letter-spacing: 0.5px; margin-bottom: 4px; }
  .service-list { list-style: none; }
  .service-list li { display: flex; align-items: center; height: 33.4px; font-size: 22px; color: var(--ink); white-space: nowrap; }
  .service-list svg { width: 15px; height: 15px; margin: 0 14px 0 6px; flex: none; }
  .quote-note { margin-top: 10px; font-size: 19.5px; line-height: 25px; color: var(--gold); width: 560px; }
  .rule { position: absolute; left: 0; top: 980px; width: 1049px; height: 4px; background: var(--gold); }
  .footer {
    position: absolute; left: 0; top: 992px; width: 1049px; height: 208px;
    background: radial-gradient(ellipse at 30% 40%, #2a2a2a 0%, var(--black) 70%);
  }
  .brand-name { position: absolute; left: 62px; top: 40px; font-family: "Bebas Neue", sans-serif; font-size: 140px; line-height: 1; color: var(--silver); letter-spacing: 6px; }
  .contact { position: absolute; left: 506px; top: 46px; font-size: 21px; line-height: 29.5px; color: var(--footer-text); font-style: normal; white-space: nowrap; }
</style>
</head>
<body>
<div class="flyer">
  <svg class="hero" viewBox="0 0 1049 442" role="img" aria-label="Greyscale photo of a triple road train tipper truck on an outback dirt road under a cloudy sky">
    <defs>
      <linearGradient id="sky" x1="0" y1="0" x2="0" y2="1">
        <stop offset="0" stop-color="#cfcfcf"/>
        <stop offset="0.5" stop-color="#a9a9a9"/>
        <stop offset="0.62" stop-color="#5a5a5a"/>
        <stop offset="0.75" stop-color="#9d9d9d"/>
        <stop offset="1" stop-color="#b9b9b9"/>
      </linearGradient>
      <radialGradient id="shine" cx="0.45" cy="0.2" r="0.6">
        <stop offset="0" stop-color="#5a5a5a"/>
        <stop offset="1" stop-color="#0b0b0b"/>
      </radialGradient>
    </defs>
    <rect width="1049" height="442" fill="url(#sky)"/>
    <polygon points="0,0 673,0 0,143" fill="url(#shine)"/>
    <polygon points="0,420 680,384 1049,411 0,442" fill="var(--grey-dark)"/>
    <polygon points="569,381 1049,337 1049,411" fill="var(--gold)"/>
    <polygon points="0,442 1049,411 1049,442" fill="var(--paper)"/>
  </svg>

  <div class="gallery">
    <div class="gallery-photo" role="img" aria-label="Greyscale photo of a road grader and a wheel loader on a gravel yard"></div>
    <div class="gallery-photo" role="img" aria-label="Greyscale photo of prime mover trucks parked beside a dome shed"></div>
    <div class="gallery-photo" role="img" aria-label="Greyscale photo of a truck hauling a grader on a drop deck trailer"></div>
  </div>

  <section class="services">
    <h2 class="services-title">Services Include:</h2>
    <ul class="service-list">
      <li><svg viewBox="0 0 16 16"><circle cx="8" cy="8" r="6.5" fill="none" stroke="var(--gold)" stroke-width="1.6"/><path d="M6.5 5 L9.5 8 L6.5 11" fill="none" stroke="var(--gold)" stroke-width="1.8"/></svg>Over size loads / Hot Shot Loads</li>
      <li><svg viewBox="0 0 16 16"><circle cx="8" cy="8" r="6.5" fill="none" stroke="var(--gold)" stroke-width="1.6"/><path d="M6.5 5 L9.5 8 L6.5 11" fill="none" stroke="var(--gold)" stroke-width="1.8"/></svg>Heavy Vehicle Recovery services</li>
      <li><svg viewBox="0 0 16 16"><circle cx="8" cy="8" r="6.5" fill="none" stroke="var(--gold)" stroke-width="1.6"/><path d="M6.5 5 L9.5 8 L6.5 11" fill="none" stroke="var(--gold)" stroke-width="1.8"/></svg>Potable Water Deliveries</li>
      <li><svg viewBox="0 0 16 16"><circle cx="8" cy="8" r="6.5" fill="none" stroke="var(--gold)" stroke-width="1.6"/><path d="M6.5 5 L9.5 8 L6.5 11" fill="none" stroke="var(--gold)" stroke-width="1.8"/></svg>Road Building / Maintenance</li>
      <li><svg viewBox="0 0 16 16"><circle cx="8" cy="8" r="6.5" fill="none" stroke="var(--gold)" stroke-width="1.6"/><path d="M6.5 5 L9.5 8 L6.5 11" fill="none" stroke="var(--gold)" stroke-width="1.8"/></svg>Earthworks</li>
      <li><svg viewBox="0 0 16 16"><circle cx="8" cy="8" r="6.5" fill="none" stroke="var(--gold)" stroke-width="1.6"/><path d="M6.5 5 L9.5 8 L6.5 11" fill="none" stroke="var(--gold)" stroke-width="1.8"/></svg>Sand &amp; Metal Supply &amp; Cartage</li>
      <li><svg viewBox="0 0 16 16"><circle cx="8" cy="8" r="6.5" fill="none" stroke="var(--gold)" stroke-width="1.6"/><path d="M6.5 5 L9.5 8 L6.5 11" fill="none" stroke="var(--gold)" stroke-width="1.8"/></svg>Road Train Tippers</li>
      <li><svg viewBox="0 0 16 16"><circle cx="8" cy="8" r="6.5" fill="none" stroke="var(--gold)" stroke-width="1.6"/><path d="M6.5 5 L9.5 8 L6.5 11" fill="none" stroke="var(--gold)" stroke-width="1.8"/></svg>Road Train Tankers</li>
      <li><svg viewBox="0 0 16 16"><circle cx="8" cy="8" r="6.5" fill="none" stroke="var(--gold)" stroke-width="1.6"/><path d="M6.5 5 L9.5 8 L6.5 11" fill="none" stroke="var(--gold)" stroke-width="1.8"/></svg>Road Train Flat Tops</li>
      <li><svg viewBox="0 0 16 16"><circle cx="8" cy="8" r="6.5" fill="none" stroke="var(--gold)" stroke-width="1.6"/><path d="M6.5 5 L9.5 8 L6.5 11" fill="none" stroke="var(--gold)" stroke-width="1.8"/></svg>Drop Deck Trailers</li>
      <li><svg viewBox="0 0 16 16"><circle cx="8" cy="8" r="6.5" fill="none" stroke="var(--gold)" stroke-width="1.6"/><path d="M6.5 5 L9.5 8 L6.5 11" fill="none" stroke="var(--gold)" stroke-width="1.8"/></svg>Mine site accredited equipment &amp; Operators.</li>
    </ul>
    <p class="quote-note">We offer a large rage of services not listed so call us today for a personalised quote to suit your needs.</p>
  </section>

  <div class="rule"></div>

  <footer class="footer">
    <div class="brand-name">KVR</div>
    <address class="contact">
      KVR Pty Ltd<br>
      Depot: Lot 514, Banksia Flats Track Coober Pedy<br>
      Mobile: 047 216 9381<br>
      email: darren@kestrelvaleroadworks.com.au
    </address>
  </footer>
</div>
</body>
</html>
```